KVO mobile detailing

Im starting a mobile detailing company where I go to the clients looking for something that will get good attention and looks professional but also resemble what we do.

It Company

```html
<!DOCTYPE html>
<html lang="en">
<head>
<meta charset="utf-8">
<title>KVO mobile detailing – business card</title>
<link rel="stylesheet" href="https://fonts.googleapis.com/css2?family=Play:wght@400;700&display=swap">
<style>
  :root {
    --backdrop: #e8e5e0;
    --card-black: #1c1c1c;
    --card-charcoal: #2e2e2e;
    --pattern-light: #5a5a5a;
    --brand-red: #e2283c;
    --text-white: #ffffff;
    --shadow: rgba(0, 0, 0, 0.28);
  }
  * { margin: 0; padding: 0; box-sizing: border-box; }
  html, body {
    width: 1200px;
    height: 991px;
    overflow: hidden;
    background: var(--backdrop);
    font-family: "Play", sans-serif;
  }
  .canvas {
    position: relative;
    width: 1200px;
    height: 991px;
  }
  .card {
    position: absolute;
    width: 540px;
    height: 310px;
    border-radius: 4px;
    overflow: hidden;
    box-shadow: 0 10px 26px var(--shadow);
  }

  /* Front side */
  .card--front {
    left: 80px;
    top: 170px;
    background: var(--card-black);
  }
  .card__pattern {
    position: absolute;
    inset: 0;
    background:
      linear-gradient(135deg, var(--pattern-light) 0%, var(--card-black) 45%, var(--pattern-light) 75%, var(--card-black) 100%);
    opacity: 0.85;
  }
  .card__identity {
    position: absolute;
    left: 245px;
    top: 98px;
    color: var(--brand-red);
  }
  .card__name {
    font-size: 34px;
    font-weight: 400;
    line-height: 1.1;
  }
  .card__role {
    font-size: 17px;
    margin-top: 6px;
    margin-left: 6px;
  }

  /* Back side */
  .card--back {
    left: 590px;
    top: 500px;
    background: var(--card-black);
  }
  .card__texture {
    position: absolute;
    inset: 0;
    background: linear-gradient(160deg, var(--card-charcoal) 0%, var(--card-black) 60%, var(--card-charcoal) 100%);
  }
  .card__contact {
    position: absolute;
    right: 34px;
    top: 38px;
    color: var(--brand-red);
    font-size: 17px;
    line-height: 2.3;
  }
  .card__services {
    position: absolute;
    left: 34px;
    top: 108px;
    list-style: none;
    color: var(--text-white);
    font-size: 17px;
    line-height: 1.75;
  }
  .card__band {
    position: absolute;
    left: 0;
    right: 0;
    bottom: 28px;
    height: 30px;
    background: var(--brand-red);
    color: var(--text-white);
    font-size: 16px;
    line-height: 30px;
    text-align: right;
    padding-right: 30px;
  }
</style>
</head>
<body>
<main class="canvas">

  <section class="card card--front" aria-label="Business card front">
    <div class="card__pattern" role="img" aria-label="Repeating white typographic pattern of the words KVO mobile detail set at different sizes and angles"></div>
    <div class="card__identity">
      <p class="card__name">Marco Delgado</p>
      <p class="card__role">Owner/operator</p>
    </div>
  </section>

  <section class="card card--back" aria-label="Business card back">
    <div class="card__texture" role="img" aria-label="Faint dark typographic pattern of the words KVO mobile detail"></div>
    <div class="card__contact">
      <p>TEL : 555 210 4817</p>
      <p>email: hello@kvodetail.com</p>
    </div>
    <ul class="card__services">
      <li>complete interior detailing</li>
      <li>carpet dyeing</li>
      <li>exterior washing</li>
      <li>waxing, paint sealing</li>
    </ul>
    <p class="card__band">A detailing company where we come to you</p>
  </section>

</main>
</body>
</html>
```